PlumEcho Social Sharing Platform Needs a Redesign (2 pages / Design only)

PlumEcho is a popular social sharing platform for bloggers and marketers. The site has been quite popular for a few years now, but the site's design is looking quite dated. We're looking for a brand new design to give the service a facelift.

We are looking for a modern and fresh design that keeps all the existing functionality intact. Would prefer designs that incorporate the color blue in them.

We would like the two attached screenshots to be redesigned and submitted - using he same content. Please do not submit a redesign of the front page (non-logged in version). Redesign the 2 attached pages only, and the final deliverable is these two pages as layered PSD files.

Target Market(s)

bloggers, internet marketers

Industry/Entity Type

Social

Number of Pages Required

2 page

Requirements
Must have
• All existing functionality must be intact as seen from the screenshots.
Should not have
• Please do not submit designs based on existing front page (non-logged in version). Use attached screenshots (file 1 and 2) as a guide of existing functionality.

```html
<!DOCTYPE html>
<html lang="en">
<head>
<meta charset="utf-8">
<title>PlumEcho Dashboard</title>
<link href="https://fonts.googleapis.com/css2?family=Open+Sans:wght@400;600;700&display=swap" rel="stylesheet">
<style>
:root{
  --blue:#1565b0;
  --ink:#222;
  --line:#d9dde2;
  --panel:#3b4652;
  --soft:#f4f4f4;
  --soft-blue:#f3f7fb;
  --notice:#f8f0c0;
  --notice-line:#e4d48a;
  --footer:#4a4a4a;
  --outside:#000;
  --green:#8cc63f;
  --link:#1a5fa8;
}
*{box-sizing:border-box;margin:0;padding:0}
html,body{width:1200px;height:954px;overflow:hidden;background:var(--outside);font-family:"Open Sans",Arial,sans-serif;color:var(--ink)}
.page{position:absolute;left:196px;top:0;width:785px;height:954px;background:#fff}
.abs{position:absolute}
.topbar{left:0;top:0;width:785px;height:33px;background:var(--blue);border-bottom:2px solid #0b3a6a}
.brand{left:104px;top:0;width:155px;height:33px;background:#fff;display:flex;align-items:center;justify-content:center;gap:6px;font-weight:700;font-size:18px;color:var(--blue);letter-spacing:.3px}
.brand i{width:10px;height:10px;background:var(--blue);display:block}
.logout{left:482px;top:11px;color:#fff;font-size:10px;font-weight:600;display:flex;gap:5px;align-items:center}
.user{left:567px;top:6px;display:flex;align-items:center;gap:10px;color:#fff;font-size:10px}
.user .pic{width:24px;height:24px;border-radius:50%;background:linear-gradient(#c9a88a,#8a6a52)}
.user-bar{left:567px;top:31px;width:84px;height:3px;background:#3bd14a}
.nav{left:103px;top:50px;display:flex;gap:17px;font-size:10px;color:#111;white-space:nowrap}
.nav span{padding-bottom:6px}
.nav .on{border-bottom:2px solid var(--blue)}
.notice{left:103px;top:82px;width:428px;height:30px;background:var(--notice);border:1px solid var(--notice-line);display:flex;align-items:center;font-size:10px;color:#8a6d1c}
.notice .ic{width:22px;height:18px;background:#e8a03a;margin:0 12px 0 8px;display:flex;align-items:center;justify-content:center}
.featured{left:103px;top:128px;width:428px;height:197px;border:2px solid var(--blue)}
.featured h2{background:var(--blue);color:#fff;font-size:10px;font-weight:700;height:27px;line-height:27px;padding-left:12px}
.grid{display:grid;grid-template-columns:repeat(8,51.3px);padding:13px 0 0 8px;row-gap:10px}
.member{display:flex;flex-direction:column;align-items:center;font-size:7px;color:#333}
.member .av{width:38px;height:38px;border:1px solid var(--line);margin-bottom:3px}
.btn{background:var(--blue);color:#fff;font-size:6.5px;font-weight:700;padding:1px 5px;margin-top:2px}
.btn.buy{background:var(--green)}
.a1{background:#3a8fcf}.a2{background:#5a6e84}.a3{background:#b07a52}.a4{background:linear-gradient(135deg,#f3c64a,#6fbf5b,#4a90d9,#d45c8a)}
.a5{background:#8d6d5a}.a6{background:#9c4a3e}.a7{background:#a8845e}.a8{background:#3c2f2f}.a0{background:#d8d8d8}
.filter{left:103px;top:343px;width:428px;height:99px;background:var(--panel)}
.filter .inner{position:absolute;left:18px;top:17px;width:392px;height:64px;background:#fff;font-size:8px}
.sel{position:absolute;height:18px;border:1px solid var(--line);padding:3px 8px;color:#333;white-space:nowrap}
.tweet-av{left:103px;width:35px;height:35px;border:3px solid #fff;box-shadow:0 0 0 1px var(--line)}
.tweet{left:147px;width:384px;background:var(--soft);border:1px solid var(--line);font-size:8.5px}
.tweet .body{padding:26px 0 0 26px;height:78px;line-height:1.25}
.tweet .body b{font-weight:700}
.tweet a{color:var(--link);text-decoration:none}
.tweet .acts{position:absolute;left:0;bottom:0;width:100%;height:39px;background:#fff;display:flex;align-items:center;padding-left:24px;gap:13px;font-size:8px;color:var(--link);white-space:nowrap}
.tweet .acts .soc{display:flex;gap:3px;align-items:center;color:#333;font-size:7px}
.tag{background:var(--blue);color:#fff;font-size:6.5px;font-weight:600}
.cnt{border:1px solid #bbb;padding:0 3px;background:#fff}
.tweet.hot{border:1.5px solid #3a8fd9;background:var(--soft-blue)}
.flag{left:130px;top:647px;width:17px;height:66px;background:#3a8fd9;color:#fff;font-size:7px;writing-mode:vertical-rl;transform:rotate(180deg);display:flex;align-items:center;justify-content:center}
.credits{left:543px;top:81px;width:138px;height:114px;background:var(--blue);color:#fff;text-align:center;padding-top:18px}
.credits .num{font-size:22px;line-height:26px}
.credits p{font-size:11px;line-height:15px}
.engage{left:543px;top:207px;width:138px;height:183px;background:var(--soft-blue);font-size:8px;text-align:center;padding-top:10px;color:#333}
.egrid{display:grid;grid-template-columns:repeat(3,43px);justify-content:center;margin-top:8px;row-gap:6px}
.sites{left:543px;top:406px;width:138px;height:372px;border:1px solid var(--line)}
.sites h3{background:#555;color:#fff;font-size:8.5px;font-weight:400;text-align:center;height:20px;line-height:20px}
.site{padding:0 9px;font-size:7px;color:#333}
.site h4{font-size:8.5px;font-weight:400;margin:9px 0 5px}
.shot{height:89px;border:1px solid var(--line)}
.footer{left:0;top:896px;width:785px;height:58px;background:var(--footer);color:#ddd;font-size:7px;text-align:center;padding-top:17px;line-height:13px}
.totop{left:722px;top:867px;width:63px;height:28px;background:var(--blue);color:#fff;font-size:8px;text-align:center;line-height:9.5px;padding-top:4px}
</style>
</head>
<body>
<div class="page">
  <div class="abs topbar"></div>
  <div class="abs brand"><i></i>PlumEcho</div>
  <div class="abs logout">Logout
    <svg width="10" height="10" viewBox="0 0 10 10"><rect x="1" y="4" width="8" height="6" fill="#fff"/><path d="M3 4V2.5a2 2 0 0 1 4 0" stroke="#fff" fill="none"/></svg></div>
  <div class="abs user"><div class="pic" role="img" aria-label="Member profile photo"></div>Milorenner</div>
  <div class="abs user-bar"></div>

  <nav class="abs nav">
    <span class="on">DASHBOARD</span><span>CHIRPLY FOLLOWERS</span><span>SUBMIT TWEET</span><span>ACTIVITY SUMMARY</span><span>BUY CREDOTS</span><span>SETTINGS</span><span>AFFILIATES</span>
  </nav>

  <div class="abs notice"><div class="ic"><svg width="12" height="10" viewBox="0 0 12 10"><path d="M1 3h3l6-3v10L4 7H1z" fill="#fff"/></svg></div>See who won our contest Click here</div>

  <section class="abs featured">
    <h2>Featured Tweet</h2>
    <div class="grid">
      <div class="member"><div class="av a1" role="img" aria-label="Member avatar"></div>name here<span class="btn">follow</span></div>
      <div class="member"><div class="av a2" role="img" aria-label="Member avatar"></div>name here<span class="btn">follow</span></div>
      <div class="member"><div class="av a3" role="img" aria-label="Member avatar"></div>name here<span class="btn">follow</span></div>
      <div class="member"><div class="av a4" role="img" aria-label="Member avatar"></div>name here<span class="btn">follow</span></div>
      <div class="member"><div class="av a5" role="img" aria-label="Member avatar"></div>name here<span class="btn">follow</span></div>
      <div class="member"><div class="av a6" role="img" aria-label="Member avatar"></div>name here<span class="btn">follow</span></div>
      <div class="member"><div class="av a7" role="img" aria-label="Member avatar"></div>name here<span class="btn">follow</span></div>
      <div class="member"><div class="av a8" role="img" aria-label="Member avatar"></div>name here<span class="btn">follow</span></div>
      <div class="member"><div class="av a1" role="img" aria-label="Member avatar"></div>name here<span class="btn">follow</span></div>
      <div class="member"><div class="av a2" role="img" aria-label="Member avatar"></div>name here<span class="btn">follow</span></div>
      <div class="member"><div class="av a3" role="img" aria-label="Member avatar"></div>name here<span class="btn">follow</span></div>
      <div class="member"><div class="av a4" role="img" aria-label="Member avatar"></div>name here<span class="btn">follow</span></div>
      <div class="member"><div class="av a5" role="img" aria-label="Member avatar"></div>name here<span class="btn">follow</span></div>
      <div class="member"><div class="av a6" role="img" aria-label="Member avatar"></div>name here<span class="btn">follow</span></div>
      <div class="member"><div class="av a7" role="img" aria-label="Member avatar"></div>name here<span class="btn">follow</span></div>
      <div class="member"><div class="av a0" role="img" aria-label="Empty featured slot"></div>name here<span class="btn buy">buy</span></div>
    </div>
  </section>

  <section class="abs filter">
    <div class="inner">
      <b style="position:absolute;left:17px;top:13px;font-weight:700">Oorder by:</b>
      <div class="sel" style="left:70px;top:9px;width:83px">Most Recent</div>
      <div class="sel" style="left:158px;top:9px;width:125px">All categories</div>
      <div class="sel" style="left:16px;top:34px;width:345px">Search (keyword or Chirply handle)</div>
      <div style="position:absolute;left:361px;top:34px;width:22px;height:18px;background:#c9cdd2">
        <svg width="22" height="18" viewBox="0 0 22 18"><circle cx="10" cy="8" r="4" stroke="#fff" stroke-width="1.5" fill="none"/><path d="M13 11l3 3" stroke="#fff" stroke-width="1.5"/></svg></div>
    </div>
  </section>

  <div class="abs tweet-av a2" style="top:464px" role="img" aria-label="Member avatar"></div>
  <article class="abs tweet" style="top:463px;height:116px">
    <div class="body"><b>@BlogAheadHQ</b> is offering 35 credits to promote this (<b>Affiliates</b>)<br>Here's how to become a trustworthy affiliate <a>http://dekshr.io/7pQ2Xa</a> via<br>@DeckShare</div>
    <div class="acts"><span>↻ Report Tweet</span><span>➜ Skip this</span><span>↻ Shedule Retweet</span><span class="soc" style="margin-left:18px"><span class="tag" style="padding:1px 4px">Like</span><span class="cnt">11</span></span><span class="soc" style="margin-left:4px"><span class="cnt" style="color:#c33">+1</span><span class="cnt">6</span></span></div>
  </article>

  <div class="abs tweet-av a7" style="top:599px" role="img" aria-label="Member avatar"></div>
  <div class="abs flag">Featured Tweet</div>
  <article class="abs tweet hot" style="top:598px;height:115px">
    <div class="body" style="padding-top:20px"><b>@BlogAheadHQ</b> is offering 35 credits to promote this (<b>Affiliates</b>)<br>Here's how to become a trustworthy affiliate <a>http://dekshr.io/7pQ2Xa</a> via<br>@DeckShare</div>
    <div class="acts"><span>↻ Report Tweet</span><span>➜ Skip this</span><span>↻ Shedule Retweet</span><span class="soc" style="margin-left:18px"><span class="tag" style="padding:1px 4px">Like</span><span class="cnt">11</span></span><span class="soc" style="margin-left:4px"><span class="cnt" style="color:#c33">+1</span><span class="cnt">6</span></span></div>
  </article>

  <div class="abs tweet-av a3" style="top:732px" role="img" aria-label="Member avatar"></div>
  <article class="abs tweet" style="top:731px;height:116px">
    <div class="body"><b>@BlogAheadHQ</b> is offering 35 credits to promote this (<b>Affiliates</b>)<br>Here's how to become a trustworthy affiliate <a>http://dekshr.io/7pQ2Xa</a> via<br>@DeckShare</div>
    <div class="acts"><span>↻ Report Tweet</span><span>➜ Skip this</span><span>↻ Shedule Retweet</span><span class="soc" style="margin-left:18px"><span class="tag" style="padding:1px 4px">Like</span><span class="cnt">11</span></span><span class="soc" style="margin-left:4px"><span class="cnt" style="color:#c33">+1</span><span class="cnt">6</span></span></div>
  </article>

  <svg class="abs" style="left:326px;top:863px" width="18" height="18" viewBox="0 0 18 18" aria-label="Loading">
    <g stroke="#555" stroke-width="2" stroke-linecap="round">
      <path d="M9 1v4"/><path d="M9 13v4" opacity=".5"/><path d="M1 9h4" opacity=".7"/><path d="M13 9h4" opacity=".3"/>
      <path d="M3.3 3.3l2.8 2.8" opacity=".85"/><path d="M11.9 11.9l2.8 2.8" opacity=".4"/><path d="M3.3 14.7l2.8-2.8" opacity=".6"/><path d="M11.9 6.1l2.8-2.8" opacity=".2"/>
    </g></svg>

  <aside class="abs credits">
    <div class="num">315959</div>
    <p>YOUR CREDITS</p>
    <p><b>click here</b> to submit</p>
    <p style="font-size:13px;line-height:17px">A Retweet</p>
  </aside>

  <aside class="abs engage">
    Engage with other members<br>who have recently shared<br>your tweets
    <div class="egrid">
      <div class="member"><div class="av a0" style="width:30px;height:30px" role="img" aria-label="Member avatar placeholder"></div>name<span class="btn">follow</span></div>
      <div class="member"><div class="av a0" style="width:30px;height:30px" role="img" aria-label="Member avatar placeholder"></div>name<span class="btn">follow</span></div>
      <div class="member"><div class="av a0" style="width:30px;height:30px" role="img" aria-label="Member avatar placeholder"></div>name<span class="btn">follow</span></div>
      <div class="member"><div class="av a0" style="width:30px;height:30px" role="img" aria-label="Member avatar placeholder"></div>name<span class="btn">follow</span></div>
      <div class="member"><div class="av a0" style="width:30px;height:30px" role="img" aria-label="Member avatar placeholder"></div>name<span class="btn">follow</span></div>
      <div class="member"><div class="av a0" style="width:30px;height:30px" role="img" aria-label="Member avatar placeholder"></div>name<span class="btn">follow</span></div>
    </div>
  </aside>

  <aside class="abs sites">
    <h3>Featured Websites</h3>
    <div class="site">
      <h4>Market Chatter</h4>
      <div class="shot" style="background:linear-gradient(#5a7fa8,#2e4a6e)" role="img" aria-label="Screenshot of the Market Chatter website"></div>
      <p style="margin-top:8px;line-height:9.5px">Business resource &amp; tips for Start Ups, SME's &amp; Entrepreneurs. Business experts, for the business community.</p>
      <div style="border-top:1px solid var(--line);margin-top:10px"></div>
      <h4>SEO Training &amp; Internet<br>Marketing Blog</h4>
      <div class="shot" style="background:linear-gradient(#e9ecef,#c9563c)" role="img" aria-label="Screenshot of an SEO training blog"></div>
      <p style="margin-top:7px;line-height:9.5px">SEO Training Blog, With Free SEO Tools, Unique Strategies &amp; Free Video Tutorials</p>
    </div>
  </aside>

  <div class="abs totop">BACK<br>TO TOP</div>

  <footer class="abs footer">
    Dashboard &nbsp; | &nbsp;Chirply Followers &nbsp;| &nbsp;Submit Tweet &nbsp;| &nbsp;Activity Summary &nbsp;| &nbsp;Buy Credots &nbsp;| &nbsp;Settings &nbsp;| &nbsp;Affiliates<br>© 2014. All Rights Reserved
  </footer>
</div>
</body>
</html>
```